Brightwave Travel and Tours

Hotel Reservations
Airline Ticketing
Day Tour

My business is a Travel agency. My services are issuing domestic and international tickets. Book room/hotel reservations local/international.
My color preference is apple green/orange/red/blue.
Images of beaches, tickets,luggage.

```html
<!DOCTYPE html>
<html lang="en">
<head>
<meta charset="utf-8">
<title>Brightwave Travel and Tours – Business Card</title>
<link rel="stylesheet" href="https://fonts.googleapis.com/css2?family=Source+Sans+3:wght@400;600;700&display=swap">
<style>
  :root {
    --page-bg: #eceae6;
    --card-white: #ffffff;
    --card-dark: #2a2a2c;
    --brand-blue: #166f96;
    --sky-blue: #1aa6dc;
    --deep-blue: #116a8f;
    --ink: #2b2b2b;
    --muted: #3a3a3a;
    --accent-yellow: #f2d21b;
  }
  * { box-sizing: border-box; margin: 0; padding: 0; }
  html, body { width: 1200px; height: 900px; overflow: hidden; }
  body {
    background: var(--page-bg);
    font-family: "Source Sans 3", Arial, sans-serif;
    color: var(--ink);
    position: relative;
  }
  .card {
    position: absolute;
    left: 280px;
    width: 640px;
    height: 366px;
    border-radius: 3px;
    box-shadow: 0 6px 18px rgba(0,0,0,0.18);
    overflow: hidden;
  }
  .card--back { top: 62px; background: var(--card-dark); }
  .card--front { top: 472px; background: var(--card-white); }

  /* brand name block */
  .brand {
    position: absolute;
    display: flex;
    align-items: center;
    gap: 14px;
    color: var(--brand-blue);
    font-weight: 700;
  }
  .brand__dot {
    width: 46px; height: 46px;
    border-radius: 50%;
    background: var(--sky-blue);
    flex: none;
  }
  .brand__name { line-height: 1; text-transform: uppercase; letter-spacing: 1px; }
  .brand__main { display: block; font-size: 38px; }
  .brand__sub { display: block; font-size: 19px; margin-top: 4px; letter-spacing: 2px; }

  .card--back .brand { left: 50%; top: 118px; transform: translateX(-50%); }
  .services {
    position: absolute;
    left: 0; right: 0;
    top: 232px;
    text-align: center;
    color: var(--brand-blue);
    font-size: 17px;
    letter-spacing: 0.3px;
  }
  .services__sep { color: var(--accent-yellow); margin: 0 6px; }

  /* front */
  .front-art { position: absolute; inset: 0; }
  .person { position: absolute; left: 62px; top: 26px; }
  .person__name { font-size: 24px; font-weight: 700; line-height: 1.1; }
  .person__first { color: var(--sky-blue); }
  .person__last { color: var(--deep-blue); }
  .person__role { font-size: 15px; color: var(--muted); margin-top: 2px; }

  .address {
    position: absolute; left: 40px; top: 140px;
    font-size: 16px; line-height: 1.2; color: var(--ink); font-style: normal;
  }
  .contacts { position: absolute; left: 26px; top: 192px; list-style: none; }
  .contacts li {
    display: flex; align-items: center; gap: 8px;
    font-size: 16px; line-height: 1.2; color: var(--ink);
  }
  .contacts svg { width: 11px; height: 11px; fill: var(--deep-blue); flex: none; }

  .card--front .brand { left: 330px; top: 172px; }
  .card--front .brand__main { font-size: 34px; }
  .card--front .brand__sub { font-size: 17px; }
  .card--front .brand__dot { width: 42px; height: 42px; }
</style>
</head>
<body>

<section class="card card--back" aria-label="Card back">
  <div class="brand">
    <span class="brand__dot"></span>
    <span class="brand__name">
      <span class="brand__main">Brightwave</span>
      <span class="brand__sub">Travel and Tours</span>
    </span>
  </div>
  <p class="services">
    Hotel Reservations<span class="services__sep">|</span>Airline Ticketing<span class="services__sep">|</span>Day Tour
  </p>
</section>

<section class="card card--front" aria-label="Card front">
  <svg class="front-art" width="640" height="366" viewBox="0 0 640 366" aria-hidden="true">
    <polygon points="16,24 48,24 16,58" fill="var(--sky-blue)"/>
    <polygon points="34,58 54,24 56,58" fill="var(--deep-blue)"/>
    <polygon points="0,268 312,268 300,290 0,290" fill="var(--sky-blue)"/>
    <polygon points="322,296 640,296 640,346 296,346" fill="var(--deep-blue)"/>
  </svg>

  <div class="person">
    <p class="person__name"><span class="person__first">Daniel</span> <span class="person__last">Reyes</span></p>
    <p class="person__role">Managing Director</p>
  </div>

  <address class="address">
    48 Harbourview Road<br>
    Marina District, 40512
  </address>

  <ul class="contacts">
    <li>
      <svg viewBox="0 0 12 12"><path d="M2 1h3l1 3-1.5 1a7 7 0 0 0 3 3L8.5 7l3 1v3c-6 0-10-4-10-10z"/></svg>
      044-555 201 734
    </li>
    <li>
      <svg viewBox="0 0 12 12"><rect x="2" y="0" width="8" height="4"/><rect x="0" y="4" width="12" height="6" rx="1"/><rect x="3" y="8" width="6" height="4" fill="#fff"/></svg>
      044-555 201 735
    </li>
    <li>
      <svg viewBox="0 0 12 12"><rect x="0" y="2" width="12" height="8"/><path d="M0 2l6 5 6-5" fill="none" stroke="#fff" stroke-width="1"/></svg>
      hello@brightwavetours.com
    </li>
  </ul>

  <div class="brand">
    <span class="brand__dot"></span>
    <span class="brand__name">
      <span class="brand__main">Brightwave</span>
      <span class="brand__sub">Travel and Tours</span>
    </span>
  </div>
</section>

</body>
</html>
```